Vandrel Group — Business Card Design Brief
Overview
Design a double-sided business card for Vandrel Group that highlights our two service arms: Vandrel Communications (telecommunications) and Vandrel Energy (business energy solutions). The card should feel smart and stand out when handed to clients.

Objectives
Showcase our areas of specialty clearly.
Reflect the overall Vandrel / Vandrel Group brand while acknowledging both arms.
Explore using both logos (Communications + Energy) or one unified logo, depending on the design.

Deliverables
One double-sided business card design (front + back).

Content & Copy
Front (preferred): Logo: Vandrel / Vandrel Group
Descriptor: Business Communications | Business Energy
Back:My contact details and company details
Core products: Business Mobile • Telephony • Internet • Business Energy Solutions

Brand & Visual Direction
We have a group logo currently tailored more toward telecoms, plus a separate Vandrel Energy logo.
Please explore layouts that use both logos or just one, whichever works best.
Color: I wouldn't mind seeing an option using our the Blue/Purple gradient from our website (vandrel-example.co.uk), but also open to non-gradient approaches and other colours..

Overall look: Smart, modern, and distinctive.
Format & Print Specs
Double-sided business card format. (Use a standard size

Must-Haves
Front: Vandrel wording or Vandrel Group wording with atleast 1 logo also on front “Business Communications | Business Energy.”

Back: Contact + company details and core products.
A design that stands out while remaining professional.

Nice-to-Have Options
A gradient version using our site’s Blue/Purple gradient.
A non-gradient version.
A dual-logo treatment versus a single-logo treatment.

Thanks
Dominic

```html
<!DOCTYPE html>
<html lang="en">
<head>
<meta charset="utf-8">
<title>Vandrel Group — Business Card</title>
<link rel="stylesheet" href="https://fonts.googleapis.com/css2?family=Poppins:wght@700&family=Arimo:wght@400;700&display=swap">
<style>
  :root {
    --page: #e4e4e4;
    --card: #303030;
    --ink: #ffffff;
    --ink-soft: #e8e8e8;
    --emboss: #3a3a3a;
    --emboss-line: #262626;
    --green: #5cb82a;
    --blue: #1f7ae0;
    --energy-text: #7fbf1f;
    --comms-text: #1e8fe6;
    --divider: #8a8a8a;
  }
  * { margin: 0; padding: 0; box-sizing: border-box; }
  html, body { width: 1200px; height: 1200px; overflow: hidden; background: var(--page); }
  body { position: relative; font-family: "Arimo", Arial, sans-serif; color: var(--ink); }

  .card {
    position: absolute;
    width: 689px;
    height: 393px;
    background: var(--card);
    box-shadow: 0 14px 22px rgba(0,0,0,0.22);
  }
  .card--details { left: 267px; top: 159px; }
  .card--brands { left: 262px; top: 653px; }

  .wordmark {
    font-family: "Poppins", Arial, sans-serif;
    font-weight: 700;
    color: var(--ink);
    letter-spacing: 0.5px;
    line-height: 1;
    white-space: nowrap;
  }
  .card--details .wordmark { position: absolute; left: 45px; top: 54px; font-size: 48px; }

  .person { position: absolute; left: 45px; top: 130px; }
  .person__name { font-size: 26px; font-weight: 700; letter-spacing: 0.5px; line-height: 1; }
  .person__role { font-size: 16px; margin-top: 6px; color: var(--ink-soft); }

  .address { position: absolute; left: 45px; top: 196px; font-size: 17px; line-height: 21px; color: var(--ink-soft); font-style: normal; }

  .contacts { position: absolute; left: 45px; top: 253px; list-style: none; }
  .contacts li { display: flex; align-items: center; height: 20.5px; font-size: 17px; color: var(--ink-soft); }
  .contacts svg { width: 14px; height: 14px; margin-right: 12px; fill: var(--ink); flex: none; }

  .products { position: absolute; left: 45px; top: 352px; font-size: 17.5px; color: var(--ink-soft); white-space: nowrap; }

  .emboss-mark { position: absolute; left: 290px; top: 140px; width: 340px; height: 200px; overflow: visible; }

  .divider { position: absolute; left: 355px; top: 82px; width: 1.5px; height: 227px; background: var(--divider); }

  .lockup { position: absolute; top: 96px; width: 330px; text-align: center; }
  .lockup--energy { left: 40px; }
  .lockup--comms { left: 370px; }
  .lockup__dot { display: block; margin: 0 auto; width: 122px; height: 122px; border-radius: 50%; }
  .lockup--energy .lockup__dot { background: var(--green); }
  .lockup--comms .lockup__dot { background: var(--blue); }
  .lockup .wordmark { font-size: 50px; margin-top: 22px; }
  .lockup__tagline { margin-top: 10px; font-size: 16px; text-transform: uppercase; white-space: nowrap; }
  .lockup--energy .lockup__tagline { color: var(--comms-text); letter-spacing: 0; }
  .lockup--comms .lockup__tagline { color: var(--energy-text); letter-spacing: 3px; }
</style>
</head>
<body>

<section class="card card--details" aria-label="Card front: contact details">
  <div class="wordmark">VANDREL</div>

  <div class="person">
    <p class="person__name">MARCUS HALE</p>
    <p class="person__role">President</p>
  </div>

  <address class="address">412 Alder Crescent<br>Halford, Canada 20817</address>

  <ul class="contacts">
    <li><svg viewBox="0 0 24 24"><path d="M6.6 10.8a15.2 15.2 0 0 0 6.6 6.6l2.2-2.2c.3-.3.7-.4 1-.2 1.1.4 2.3.6 3.6.6.6 0 1 .4 1 1V20c0 .6-.4 1-1 1A17 17 0 0 1 3 4c0-.6.4-1 1-1h3.5c.6 0 1 .4 1 1 0 1.3.2 2.5.6 3.6.1.3 0 .7-.2 1z"/></svg>555-210-4478</li>
    <li><svg viewBox="0 0 24 24"><path d="M7 1h10a2 2 0 0 1 2 2v18a2 2 0 0 1-2 2H7a2 2 0 0 1-2-2V3a2 2 0 0 1 2-2zm0 3v15h10V4z"/></svg>555-386-9021</li>
    <li><svg viewBox="0 0 24 24"><path d="M2 5h20v14H2zm2 2v.5l8 5 8-5V7l-8 5z"/></svg>info@vandrel-example.com</li>
    <li><svg viewBox="0 0 24 24"><path d="M12 2a10 10 0 1 0 0 20 10 10 0 0 0 0-20zm-1 17.9A8 8 0 0 1 4.2 10L9 14.8v1.1c0 1.1.9 2 2 2zm6.9-2.5a2 2 0 0 0-1.9-1.4h-1v-3c0-.6-.4-1-1-1H8v-2h2c.6 0 1-.4 1-1V7h2a2 2 0 0 0 2-2v-.4a8 8 0 0 1 2.9 12.8z"/></svg>www.vandrel-example.com</li>
  </ul>

  <svg class="emboss-mark" viewBox="0 0 340 200" role="img" aria-label="Faint embossed brand circle with name">
    <circle cx="103" cy="97" r="92" fill="var(--emboss)" stroke="var(--emboss-line)" stroke-width="2"/>
    <text x="208" y="106" font-family="Poppins, Arial, sans-serif" font-weight="700" font-size="22" textLength="122" lengthAdjust="spacingAndGlyphs" fill="var(--emboss)">VANDREL</text>
  </svg>

  <p class="products">Business Mobile &nbsp;•&nbsp; Telephony &nbsp;•&nbsp; Internet &nbsp;•&nbsp; Business Energy Solutions</p>
</section>

<section class="card card--brands" aria-label="Card back: brand lockups">
  <div class="lockup lockup--energy">
    <span class="lockup__dot"></span>
    <div class="wordmark">VANDREL</div>
    <p class="lockup__tagline">Business Communications</p>
  </div>

  <div class="divider"></div>

  <div class="lockup lockup--comms">
    <span class="lockup__dot"></span>
    <div class="wordmark">VANDREL</div>
    <p class="lockup__tagline">Business Energy</p>
  </div>
</section>

</body>
</html>
```